Brightwell Giving Inc

We need a full re-design of our non-profit organization website (www.brightwellgiving.org). Ideally, we are looking to make it more attractive, user-friendly, and interactive with our business model.

Please make sure to user colors that ago with our logo.

We need a homepage done and we also need a content page done where we will use for the other pages to fill with content.

Target Market(s)

Clothes/textiles donations.

Industry/Entity Type

Charity

Number of Pages Required

2 page

Colors

Designer to choose colors to be used in the design.

Requirements
Must have
• It must match the styling of our logo and same colors as current website. (www.brightwellgiving.org)
Nice to have
• Sleek homepage that is easy to understand and get our main points across.

```html
<!DOCTYPE html>
<html lang="en">
<head>
<meta charset="utf-8">
<title>Brightwell Giving – Home</title>
<link href="https://fonts.googleapis.com/css2?family=Raleway:wght@300;400;500;600;700;800&family=Roboto:wght@400;500&display=swap" rel="stylesheet">
<style>
:root{
  --green:#3f9c0b;
  --green-dark:#2f8510;
  --green-text:#3a9a0c;
  --yellow:#f3ea1a;
  --white:#ffffff;
  --grey-text:#8c8c8c;
  --red:#db4437;
  --photo-a:#5f8d3c;
  --photo-b:#8ab85a;
  --store-a:#6d7480;
  --store-b:#c9b9a6;
  --map-a:#e6ecd9;
  --map-b:#cfe0c0;
}
*{margin:0;padding:0;box-sizing:border-box}
html,body{width:1200px;height:1200px;overflow:hidden;background:var(--white);font-family:'Raleway',sans-serif}
.page{position:relative;width:1200px;height:1200px}
.abs{position:absolute}

.site-header{left:0;top:0;width:1200px;height:67px;background:var(--white)}
.brand{left:200px;top:18px;display:flex;align-items:center;gap:8px}
.brand-mark{width:44px;height:44px;background:var(--green)}
.brand-name{font-weight:700;font-size:20px;color:var(--green-dark);letter-spacing:.5px;line-height:1}
.brand-tag{font-size:10.5px;color:#222;margin-top:6px;font-family:'Roboto',sans-serif}

.hero{left:0;top:67px;width:1200px;height:357px;background:var(--green)}
.main-nav{left:200px;top:88px;display:flex;gap:32px;font-size:12.5px;letter-spacing:.4px;color:var(--white);font-weight:500}
.main-nav .active{color:var(--yellow)}
.hero-photo{left:199px;top:144px;width:451px;height:259px;border:3px solid var(--white);box-shadow:0 3px 6px rgba(0,0,0,.3);background:radial-gradient(ellipse at center,var(--photo-b),var(--photo-a))}
.hero-title{left:673px;top:132px;width:310px;text-align:center;font-size:48px;font-weight:700;color:var(--white)}
.hero-text{left:673px;top:190px;width:310px;font-size:11.6px;line-height:14.4px;font-weight:300;color:var(--white)}
.dots{left:752px;top:367px;display:flex;gap:38px}
.dot{width:22px;height:22px;border:2px solid var(--white);border-radius:50%;position:relative}
.dot.on::after{content:"";position:absolute;left:4px;top:4px;width:10px;height:10px;border-radius:50%;background:var(--white)}

.tab{top:432px;width:134px;height:40px;border-radius:20px;background:var(--green);color:var(--white);font-size:12.5px;font-weight:500;display:flex;align-items:center;justify-content:center}

.who-title{left:200px;top:488px;font-size:17px;font-weight:800;letter-spacing:3px;color:var(--green-text)}
.who-list{left:200px;top:512px;list-style:none;font-size:9.8px;color:var(--grey-text);font-weight:400}
.who-list li{height:23px}
.motto{left:201px;top:672px;font-size:16.5px;font-weight:700;color:var(--green-text);line-height:20px}
.find{left:267px;top:746px;font-size:16px;font-weight:700;color:var(--green-text);display:flex;align-items:center;gap:4px}
.zip{left:200px;top:764px;font-size:16px;font-weight:700;color:var(--green-text)}
.search{left:200px;top:790px;width:350px;height:32px;border-radius:16px;background:var(--white);box-shadow:0 2px 4px rgba(0,0,0,.35);display:flex;align-items:center;justify-content:center;color:#c9c9c9;font-size:16px;font-weight:600}
.search svg{position:absolute;right:16px;top:6px}

.store-photo{left:591px;top:484px;width:408px;height:340px;border:2px solid #ccc;background:linear-gradient(180deg,var(--store-a) 0%,var(--store-a) 45%,var(--store-b) 100%)}

.map-panel{left:202px;top:845px;width:256px;height:260px;background:var(--white);border-left:1px solid var(--green)}
.map-head{height:38px;background:var(--red);color:var(--white);font-family:'Roboto',sans-serif;font-size:12px;display:flex;align-items:center;padding-left:50px;position:relative}
.map-head .menu{position:absolute;left:20px;top:15px;width:12px;height:8px;border-top:1.5px solid #fff;border-bottom:1.5px solid #fff}
.map-head .menu::after{content:"";position:absolute;left:0;top:2px;width:12px;border-top:1.5px solid #fff}
.map-info{padding:10px 0 0 50px;font-family:'Roboto',sans-serif;font-size:8.5px;color:#333;height:58px;background:#f7f7f7;line-height:13px}
.map-info .views{color:#888;font-size:8px}
.map-info .share{color:#3367d6;font-weight:500;font-size:8px}
.layer{font-family:'Roboto',sans-serif;font-size:9px;color:#222;position:absolute;left:50px}
.check{position:absolute;left:20px;top:106px;width:12px;height:12px;background:var(--red);border-radius:2px}
.map-area{left:458px;top:845px;width:543px;height:260px;background:linear-gradient(135deg,var(--map-a),var(--map-b))}

.site-footer{left:0;top:1120px;width:1200px;height:80px;background:var(--green-dark);color:var(--white);font-weight:700}
.copyright{left:200px;top:30px;font-size:15.5px;color:#e9f3e2}
.social{left:826px;top:20px;display:flex;align-items:center;gap:18px;font-size:16px;color:#e9f3e2}
.social .circle{width:32px;height:32px;border-radius:50%;background:var(--white)}
</style>
</head>
<body>
<div class="page">

  <header class="site-header abs">
    <div class="brand abs">
      <div class="brand-mark"></div>
      <div>
        <div class="brand-name">BRIGHTWELL GIVING</div>
        <div class="brand-tag">Think Globally while Donating Locally</div>
      </div>
    </div>
  </header>

  <section class="hero abs">
  </section>
  <nav class="main-nav abs">
    <span class="active">HOME</span><span>ABOUTUS</span><span class="active">MISSIONS</span><span>HOW IT WORKS</span><span>SPONSERS</span><span>NEWS</span><span>DONATE</span><span>WALL OF NEED</span>
  </nav>
  <div class="hero-photo abs" role="img" aria-label="Volunteers holding hands in a large circle on a green lawn"></div>
  <h1 class="hero-title abs">Welcome!</h1>
  <p class="hero-text abs">Brightwell Giving is a non-profit organization that was created for one purpose: helping the less fortunate in our country’s time of greatest need. Started in 2007, Brightwell Giving has been a dedicated member of its local communities over the past four years. The company’s clothing collection efforts have allowed it to provide some of the neediest members of the community to clothe themselves and their families. The company’s goal is to ensure that some of the most basic needs of the community’s members are met thru the philanthropic efforts of the organizations members and contributors.</p>
  <div class="dots abs"><span class="dot on"></span><span class="dot"></span><span class="dot"></span></div>

  <div class="tab abs" style="left:201px">Welcome</div>
  <div class="tab abs" style="left:422px">Donation in Europe</div>
  <div class="tab abs" style="left:644px">Donation Recipients</div>
  <div class="tab abs" style="left:866px">Recent News</div>

  <h2 class="who-title abs">WHO we ARE</h2>
  <ul class="who-list abs">
    <li>-WE ARE AN OPEN BOOK ORGANIZATION</li>
    <li>- WE ARE A TRUE 501(c)(3) NON-PROFIT ORGANIZATION</li>
    <li>- OUR GOAL IS TO BE WITH AND WITHIN THE COMMUNITY</li>
    <li>- SUPPORT ANTI-GUN VIOLENCE</li>
    <li>- HELP DISASTER VICTIMS OF HURRICANE IRENE</li>
    <li>- HELP VALLEY FAMILY ALLIANCE</li>
  </ul>
  <p class="motto abs">Think globally while donating locally<br>~brightwell giving</p>

  <div class="find abs">Find Local Donation Place
    <svg width="18" height="18" viewBox="0 0 18 18"><circle cx="9" cy="9" r="9" fill="#3a9a0c"/><path d="M9 4a3.2 3.2 0 0 0-3.2 3.2C5.8 9.8 9 14 9 14s3.2-4.2 3.2-6.8A3.2 3.2 0 0 0 9 4z" fill="#fff"/><circle cx="9" cy="7.2" r="1.2" fill="#3a9a0c"/></svg>
  </div>
  <div class="zip abs">Zip:</div>
  <div class="search abs">Search
    <svg width="20" height="20" viewBox="0 0 20 20"><circle cx="8" cy="8" r="6" fill="none" stroke="#3a9a0c" stroke-width="2.6"/><line x1="12.5" y1="12.5" x2="18" y2="18" stroke="#3a9a0c" stroke-width="3" stroke-linecap="round"/></svg>
  </div>

  <div class="store-photo abs" role="img" aria-label="Thrift store and donation center storefront at its grand opening ribbon cutting"></div>

  <div class="map-panel abs">
    <div class="map-head"><span class="menu"></span>Brightwell Giving Bins</div>
    <div class="map-info">Clothes Donation Bins<br><span class="views">17,002 views</span><br><span class="share">SHARE</span></div>
    <span class="check"></span>
    <span class="layer" style="top:108px">All_LocationsShortList.xlsx</span>
    <span class="layer" style="top:132px">All items</span>
  </div>
  <div class="map-area abs" role="img" aria-label="Regional map marking donation bin locations"></div>

  <footer class="site-footer abs">
    <div class="copyright abs">© 2018 BRIGHTWELL GIVING. ALL RIGHTS RESERVED</div>
    <div class="social abs"><span class="circle"></span>Keep connected</div>
  </footer>

</div>
</body>
</html>
```